TideWillowNook.com needs updated website design.

TideWillowNook.com offers individuals a quick, hassle-free way of selling their car, rv, or boat in the Sun City Center, FL area. We will come to the customer's place of choosing in order to give them an in-person offer for their car, rv, or boat. Looking for a website design that will allow users to input their vehicle details as well as their contact info in order to schedule a time and place for our staff to come make them an offer. Currently have an active site that can be referenced.

Target Market(s)

Older people who no longer need their cars.

Industry/Entity Type

Automotive

Coding

Coded - Design and coding required

Number of Pages Required

3 page

Font styles to use
Sans Serif

Colors
a1cd3a
33b8a4

Requirements
Must have
• Trustworthy theme, Emphasis on capturing contact info (contact form visible at all times). Standard privacy policy. Wordpress theme

```html
<!DOCTYPE html>
<html lang="en">
<head>
<meta charset="utf-8">
<title>TideWillowNook.com</title>
<link href="https://fonts.googleapis.com/css2?family=Lato:ital,wght@0,400;0,700;1,400&display=swap" rel="stylesheet">
<style>
:root{
  --navy:#1e3766;
  --ink:#2e2e2e;
  --text:#3a3a3a;
  --muted:#555;
  --header-bg:#f5f7fb;
  --grey-bg:#eeeeee;
  --footer-bg:#f0f0f0;
  --white:#ffffff;
  --field-border:#bdbdbd;
}
*{box-sizing:border-box;margin:0;padding:0}
html,body{width:1200px;height:2673px;overflow:hidden}
body{font-family:'Lato',sans-serif;color:var(--ink);background:var(--white);position:relative}
a{color:inherit;text-decoration:none}
.btn{display:inline-flex;align-items:center;justify-content:center;background:var(--navy);color:var(--white);font-weight:700;font-size:15px;width:150px;height:45px;border-radius:2px}

.site-header{position:absolute;left:0;top:0;width:1200px;height:100px;background:var(--header-bg)}
.brand{position:absolute;left:150px;top:24px;display:flex;align-items:center;gap:10px;font-weight:700;font-size:19px;color:var(--navy)}
.brand-dot{width:14px;height:14px;border-radius:50%;background:#5bb8d8}
.main-nav{position:absolute;right:150px;top:29px;display:flex;gap:30px;font-size:15px;color:var(--ink)}

.hero{position:absolute;left:0;top:100px;width:1200px;height:517px;background:linear-gradient(#ffffff,#f7f7f7)}
.hero-title{position:absolute;left:150px;top:42px;font-size:39px;font-weight:700;color:#333}
.hero-sub{position:absolute;left:150px;top:92px;font-size:26px;color:#333}
.hero .btn{position:absolute;left:151px;top:139px}
.hero-photo{position:absolute;left:0;top:195px;width:1200px;height:322px;background:linear-gradient(180deg,#f5f5f3 0%,#b8b79a 30%,#6b7a5d 55%,#4f6a86 70%,#555a5d 88%,#8fa64a 100%)}

.features{position:absolute;left:0;top:617px;width:1200px;height:225px;display:flex;padding:0 120px}
.feature{flex:1;text-align:center;padding-top:45px}
.feature svg{width:64px;height:64px;stroke:var(--navy);fill:none;stroke-width:2.6;stroke-linecap:round;stroke-linejoin:round}
.feature h3{font-size:28px;font-weight:700;color:#333;margin-top:14px}
.feature p{font-size:15px;color:var(--text);margin-top:6px}

.about{position:absolute;left:0;top:842px;width:1200px;height:496px;background:var(--grey-bg)}
.about-text{position:absolute;left:150px;top:165px;width:420px}
.about-text h2{font-size:27px;font-weight:700;color:#333;margin-bottom:10px}
.about-text p{font-size:18px;line-height:30px;color:var(--text)}
.about-photo{position:absolute;left:600px;top:60px;width:450px;height:375px;background:linear-gradient(120deg,#c9d0d3 0%,#9aa39a 35%,#cfcac3 55%,#6e6e70 100%)}

.cars{position:absolute;left:0;top:1338px;width:1200px;height:434px}
.cars h2{position:absolute;top:52px;width:100%;text-align:center;font-size:28px;font-weight:700;color:#333}
.card{position:absolute;top:117px;width:285px;height:255px;background:var(--white);box-shadow:0 1px 8px rgba(0,0,0,.18);padding:20px 22px}
.card h3{font-size:22px;line-height:30px;font-weight:700;color:#333}
.card p{font-size:15px;line-height:30px;color:var(--text);margin-top:10px}
.card .btn{position:absolute;left:22px;top:188px}

.contact-zone{position:absolute;left:0;top:1772px;width:1200px;height:581px}
.map{position:absolute;inset:0;background:linear-gradient(90deg,#8d9a74 0%,#9a9580 20%,#9e9a8c 50%,#9a9686 80%,#8e9a78 100%)}
.contact-panel{position:absolute;left:150px;top:60px;width:900px;height:459px;background:var(--white)}
.contact-panel h2{text-align:center;font-size:28px;font-weight:700;color:#333;margin-top:30px}
.field{position:absolute;border:2px solid var(--field-border);font-style:italic;font-size:15px;color:#444;padding:15px 15px}
.contact-panel .btn{position:absolute;left:730px;top:376px}
.rule{position:absolute;left:0;top:2353px;width:1200px;height:3px;background:var(--navy)}

.site-footer{position:absolute;left:0;top:2356px;width:1200px;height:284px;background:var(--footer-bg)}
.site-footer .brand{top:46px}
.footer-about{position:absolute;left:150px;top:110px;width:285px;font-size:15px;line-height:22.5px;color:var(--text)}
.footer-col h4{font-size:22px;font-weight:700;color:#333;padding-bottom:8px;border-bottom:4px solid var(--navy);display:inline-block}
.footer-nav{position:absolute;left:567px;top:36px}
.footer-nav ul{list-style:none;margin-top:18px}
.footer-nav li{font-size:17px;line-height:30px;color:var(--text)}
.footer-contact{position:absolute;left:886px;top:36px}
.contact-item{position:relative;margin-top:18px}
.contact-item + .contact-item{margin-top:30px}
.contact-item svg{position:absolute;left:-41px;top:0;width:28px;height:28px;fill:var(--navy)}
.contact-item strong{display:block;font-size:17px;color:#333;line-height:30px}
.contact-item span{font-size:17px;color:var(--text);line-height:30px}
.copyright{position:absolute;left:0;top:2640px;width:1200px;height:33px;background:var(--navy);color:var(--white);font-weight:700;font-size:15px;display:flex;align-items:center;justify-content:center}
</style>
</head>
<body>
<header class="site-header">
  <a class="brand" href="#"><span>TideWillowNook.com</span><span class="brand-dot"></span></a>
  <nav class="main-nav"><a href="#">Home</a><a href="#">About</a><a href="#">Services</a><a href="#">Contact</a></nav>
</header>

<section class="hero">
  <h1 class="hero-title">Get your free in person cash offer today</h1>
  <p class="hero-sub">Don’t sell til you give me a yell</p>
  <a class="btn" href="#">Contact us</a>
  <div class="hero-photo" role="img" aria-label="Blue classic sports car parked by tall grass beside a road"></div>
</section>

<section class="features">
  <div class="feature">
    <svg viewBox="0 0 64 64"><circle cx="36" cy="32" r="22"/><path d="M36 18v14l8 6"/><path d="M4 26h10M2 34h10M6 42h10"/></svg>
    <h3>Fast</h3><p>I’ll be at your door today</p>
  </div>
  <div class="feature">
    <svg viewBox="0 0 64 64"><path d="M32 6v50M22 58h20M12 16h40"/><path d="M12 16l-8 20h16zM52 16l-8 20h16z"/><path d="M4 36a8 5 0 0016 0M44 36a8 5 0 0016 0"/></svg>
    <h3>Fair</h3><p>Get fair price for your vehicle</p>
  </div>
  <div class="feature">
    <svg viewBox="0 0 64 64"><path d="M32 4l22 8v18c0 14-10 24-22 30C20 54 10 44 10 30V12z"/><circle cx="32" cy="32" r="12"/><path d="M26 32l4 4 8-8"/></svg>
    <h3>Friendly</h3><p>Trusted for Over 25 Years</p>
  </div>
  <div class="feature">
    <svg viewBox="0 0 64 64"><path d="M14 4h26l12 12v44H14z"/><path d="M40 4v12h12M22 28h22M22 36h22M22 44h22M22 52h14"/></svg>
    <h3>Hassle Free</h3><p>I Handle All the Paperwork</p>
  </div>
</section>

<section class="about">
  <div class="about-text">
    <h2>About Us</h2>
    <p>We offer the most convenient way of selling your vehicle. We will come to you at a place of your choosing, i.e. home, office, or any other public place. We will give you an in person cash offer on the spot.</p>
  </div>
  <div class="about-photo" role="img" aria-label="Hand holding out a set of car keys"></div>
</section>

<section class="cars">
  <h2>We Are Interested In All Cars</h2>
  <article class="card" style="left:150px">
    <h3>Got an old clunker?<br>We’re interested</h3>
    <p>I’ll buy It! No matter what the issue is - Turn it into cash today!</p>
    <a class="btn" href="#">Contact us</a>
  </article>
  <article class="card" style="left:458px">
    <h3>Got a nice car you just don’t need?</h3>
    <p>I’ll buy it! – Stop wasting money on insurance, registration and maintenance costs!</p>
    <a class="btn" href="#">Contact us</a>
  </article>
  <article class="card" style="left:766px">
    <h3>Got a car that needs repairs?</h3>
    <p>I’ll buy it! – No matter what the issue is I’ll come take it away today!</p>
    <a class="btn" href="#">Contact us</a>
  </article>
</section>

<section class="contact-zone">
  <div class="map" role="img" aria-label="Regional road map of the service area"></div>
  <form class="contact-panel">
    <h2>Contact Us</h2>
    <div class="field" style="left:21px;top:86px;width:423px;height:49px">Name</div>
    <div class="field" style="left:456px;top:86px;width:423px;height:49px">Email</div>
    <div class="field" style="left:21px;top:146px;width:423px;height:49px">Phone number</div>
    <div class="field" style="left:456px;top:146px;width:423px;height:49px">Subject</div>
    <div class="field" style="left:21px;top:207px;width:858px;height:154px">Input your vehicle details</div>
    <a class="btn" href="#">Send</a>
  </form>
</section>
<div class="rule"></div>

<footer class="site-footer">
  <a class="brand" href="#"><span>TideWillowNook.com</span><span class="brand-dot"></span></a>
  <p class="footer-about">Lorem ipsum dolor sit amet, consectetur adipiscing elit. Nam tempus massa at aliquam volutpat. Morbi in mauris ultricies, bibendum massa posuere, tincidunt tortor.</p>
  <div class="footer-col footer-nav">
    <h4>Navigation</h4>
    <ul><li>Home</li><li>About</li><li>Services</li><li>Contact</li></ul>
  </div>
  <div class="footer-col footer-contact">
    <h4>Contact Us</h4>
    <div class="contact-item">
      <svg viewBox="0 0 24 24"><path d="M6.6 10.8a15 15 0 006.6 6.6l2.2-2.2a1 1 0 011-.25 11.4 11.4 0 003.6.6 1 1 0 011 1V20a1 1 0 01-1 1A17 17 0 013 4a1 1 0 011-1h3.5a1 1 0 011 1c0 1.25.2 2.45.6 3.6a1 1 0 01-.25 1z"/></svg>
      <strong>Phone Number</strong><span>813-555-0142</span>
    </div>
    <div class="contact-item">
      <svg viewBox="0 0 24 24"><path d="M2 5h20v14H2zm2 2v.5l8 6 8-6V7zm0 3v7h16v-7l-8 6z"/></svg>
      <strong>Email Address</strong><span>info@tidewillownook.com</span>
    </div>
  </div>
</footer>
<div class="copyright">TideWillowNook.com 2020 © All rights reserved.</div>
</body>
</html>
```